Advertisement Sign Project

Hi there,

I have a commercial space available for short term lease.

I need an advertisement sign to go on the double black doors (under the current Bornavel Quindrex sign).

The advertising sign should be about A3 in size and designed to attract pedestrians.

See site address at 417 Calder Parade Richmond Victoria Australia:

https://plotfinder.example-atlas.com.au/view?q=417B+Calder+Pde,+Richmond+Victoria+3121&z=17

Target Market(s)

Pop-up store tenants: fashion, textiles, bedding, furniture, homewares and kitchenwares.

The photos are provided to give you (the graphic designer) an idea of the space available.

Requirements
Must have
• Retail tenancy available for short term lease.

For all enquiries contact Owen - 0412730648 or email owen@calderparadehub.com.au

Nice to have
• Something befitting the look and feel of the building.

I was thinking a textile pattern as background, or some kind of fashion design element to inspire a potential pop up shop tenant.

```html
<!DOCTYPE html>
<html lang="en">
<head>
<meta charset="utf-8">
<title>Commercial Space Available – Short Term Lease</title>
<link rel="stylesheet" href="https://fonts.googleapis.com/css2?family=Arimo:wght@700&family=Open+Sans:wght@400&display=swap">
<style>
  :root {
    --stage: #dcdddf;
    --paper: #ffffff;
    --cyan: #00aeef;
    --magenta: #ec008c;
    --yellow: #fff200;
    --ink: #231f20;
    --grey-text: #444444;
    --bubble-pink: #ee2f8e;
  }
  html, body {
    margin: 0;
    padding: 0;
    width: 1000px;
    height: 1200px;
    overflow: hidden;
    background: var(--stage);
  }
  .poster {
    position: absolute;
    left: 97px;
    top: 18px;
    width: 813px;
    height: 1144px;
    background: var(--paper);
    overflow: hidden;
  }
  .collage {
    position: absolute;
    left: 0;
    top: 0;
    width: 813px;
    height: 1144px;
  }
  .headline {
    position: absolute;
    left: 0;
    top: 0;
    margin: 0;
    font-family: "Arimo", Arial, sans-serif;
    font-weight: 700;
  }
  .headline span {
    position: absolute;
    white-space: nowrap;
    letter-spacing: -1px;
  }
  .headline-commercial {
    left: 50px;
    top: 195px;
    font-size: 118px;
    line-height: 1;
    color: var(--cyan);
  }
  .headline-space {
    left: 48px;
    top: 300px;
    font-size: 134px;
    line-height: 1;
    color: var(--magenta);
  }
  .headline-band {
    position: absolute;
    left: 0;
    top: 449px;
    width: 540px;
    height: 90px;
  }
  .headline-available {
    left: 54px;
    top: 448px;
    font-size: 96px;
    line-height: 1;
    color: var(--ink);
  }
  .lease-bubble {
    position: absolute;
    left: 475px;
    top: 905px;
    width: 240px;
    height: 200px;
  }
  .enquiries {
    position: absolute;
    left: 0;
    right: 0;
    top: 1104px;
    margin: 0;
    text-align: center;
    font-family: "Open Sans", Arial, sans-serif;
    font-size: 17.5px;
    color: var(--grey-text);
    white-space: nowrap;
  }
</style>
</head>
<body>
  <main class="poster">
    <svg class="collage" viewBox="0 0 813 1144" aria-hidden="false">
      <g class="collage-kitchenware">
        <polygon points="640,135 780,150 782,325 655,330" fill="var(--yellow)"/>
        <rect role="img" aria-label="Photo of stacked stainless steel and gold cooking pots" x="660" y="55" width="135" height="210" rx="40" fill="#c8c8c8" opacity="0.9"/>
      </g>
      <g class="collage-bedding">
        <polygon points="495,305 610,320 600,585 490,560" fill="var(--cyan)" opacity="0.75"/>
        <polygon role="img" aria-label="Photo of a made bed with blue banded bedding" points="565,300 790,292 785,512 560,520" fill="#9aa3ab" opacity="0.8"/>
      </g>
      <g class="collage-fashion">
        <polygon points="612,520 808,532 800,740 600,725" fill="#f06ea9" opacity="0.7"/>
        <polygon role="img" aria-label="Fashion sketch of a pink ball gown" points="640,560 790,570 780,780 628,770" fill="#f4b8d3"/>
      </g>
      <g class="collage-textiles">
        <polygon role="img" aria-label="Photo of patterned fabric swatches" points="440,560 625,565 615,700 430,700" fill="#8e9296" opacity="0.8"/>
        <polygon role="img" aria-label="Blue floral textile pattern" points="418,607 590,618 580,805 440,812" fill="#6fcdf2" opacity="0.85"/>
      </g>
    </svg>

    <svg class="headline-band" viewBox="0 0 540 90" aria-hidden="true">
      <polygon points="0,0 540,0 490,90 0,90" fill="var(--yellow)"/>
    </svg>

    <h1 class="headline">
      <span class="headline-commercial">Commercial</span>
      <span class="headline-space">Space</span>
      <span class="headline-available">Available</span>
    </h1>

    <svg class="lease-bubble" viewBox="0 0 240 200" role="img" aria-label="for Short Term Lease">
      <defs>
        <linearGradient id="bubble-fill" x1="0" y1="0" x2="1" y2="1">
          <stop offset="0" stop-color="#fbd3e6"/>
          <stop offset="0.45" stop-color="var(--bubble-pink)"/>
          <stop offset="1" stop-color="#f58ac0"/>
        </linearGradient>
      </defs>
      <path d="M35,60 Q30,30 70,25 L180,10 Q205,8 210,35 L225,110 Q230,140 200,145 L80,160 L30,190 L45,150 Q15,150 20,120 Z" fill="#e9e9e9" transform="translate(8,6)"/>
      <path d="M35,60 Q30,30 70,25 L180,10 Q205,8 210,35 L225,110 Q230,140 200,145 L80,160 L30,190 L45,150 Q15,150 20,120 Z" fill="url(#bubble-fill)" stroke="#ffffff" stroke-width="3"/>
      <g transform="rotate(-22 120 95)" font-family="Arimo, Arial, sans-serif" font-weight="700" fill="#ffffff" stroke="var(--bubble-pink)" stroke-width="0.6" text-anchor="middle">
        <text x="120" y="68" font-size="20">for</text>
        <text x="122" y="100" font-size="29">Short Term</text>
        <text x="126" y="130" font-size="29">Lease</text>
      </g>
    </svg>

    <p class="enquiries">For all enquiries contact Owen - 041 2730 648 or email owen@calderparadehub.com.au</p>
  </main>
</body>
</html>
```